Business cards/stationary for physician office
Using existing logo
Bright & Fun-filled
Paul Verner, M.D.
Radiologist
Cedarpoint Imaging, LLC.
48 Quill Ridge Lane
Montgomery, TX 77490
office@brakwell-mail.net
www.cedarpointimaging-demo.com
Will contact the winning designer with actual contact info to replace above text. Please not website has not been updated with new logo, so make sure to use provided logo files.
Logo files
Logo file horizontal

```html
<!DOCTYPE html>
<html lang="en">
<head>
<meta charset="utf-8">
<title>Paul Verner, M.D. — Business Card</title>
<link rel="stylesheet" href="https://fonts.googleapis.com/css2?family=Arimo&family=Questrial&display=swap">
<style>
  :root {
    --ink-blue: #1f5ea6;
    --brand-blue: #2a4f8f;
    --ink-grey: #555a60;
    --card-light: #e4e5e7;
    --card-mid: #cdced1;
    --card-dark: #b9babd;
    --crease: rgba(255,255,255,0.55);
  }
  html, body {
    margin: 0;
    padding: 0;
    width: 1200px;
    height: 686px;
    overflow: hidden;
    background: #ffffff;
  }
  .card {
    position: relative;
    width: 1200px;
    height: 686px;
    overflow: hidden;
    background: linear-gradient(160deg, var(--card-light) 0%, var(--card-mid) 55%, var(--card-dark) 100%);
  }
  .card-shading {
    position: absolute;
    inset: 0;
    width: 1200px;
    height: 686px;
  }
  .holder-name {
    position: absolute;
    left: 22px;
    top: 52px;
    margin: 0;
    font-family: "Arimo", Arial, sans-serif;
    font-weight: 400;
    font-size: 68px;
    line-height: 1;
    color: var(--ink-blue);
    white-space: nowrap;
  }
  .holder-title {
    position: absolute;
    left: 26px;
    top: 140px;
    margin: 0;
    font-family: "Arimo", Arial, sans-serif;
    font-size: 46px;
    line-height: 1;
    color: var(--ink-grey);
  }
  .brand {
    position: absolute;
    left: 696px;
    top: 18px;
    width: 480px;
    text-align: center;
  }
  .brand-dot {
    display: block;
    width: 150px;
    height: 150px;
    margin: 0 auto;
    border-radius: 50%;
    background: var(--brand-blue);
  }
  .brand-name {
    margin: 28px 0 0;
    font-family: "Questrial", Arial, sans-serif;
    font-size: 50px;
    line-height: 1.1;
    color: var(--brand-blue);
    white-space: nowrap;
  }
  .contact-list {
    position: absolute;
    left: 12px;
    top: 484px;
    margin: 0;
    font-family: "Questrial", Arial, sans-serif;
    font-size: 31px;
    color: var(--ink-blue);
    display: grid;
    grid-template-columns: 136px auto;
    column-gap: 16px;
    row-gap: 19px;
    line-height: 1;
    white-space: nowrap;
  }
  .contact-list dt { text-align: right; margin: 0; }
  .contact-list dd { margin: 0; }
  .office-address {
    position: absolute;
    left: 690px;
    top: 478px;
    margin: 0;
    font-family: "Questrial", Arial, sans-serif;
    font-style: normal;
    font-size: 31px;
    line-height: 1.6;
    color: var(--ink-blue);
    white-space: nowrap;
  }
</style>
</head>
<body>
  <main class="card">
    <svg class="card-shading" viewBox="0 0 1200 686" aria-hidden="true">
      <defs>
        <linearGradient id="fold-light" x1="0" y1="1" x2="1" y2="0">
          <stop offset="0" stop-color="#ffffff" stop-opacity="0.35"/>
          <stop offset="1" stop-color="#ffffff" stop-opacity="0"/>
        </linearGradient>
        <linearGradient id="fold-dark" x1="1" y1="1" x2="0" y2="0">
          <stop offset="0" stop-color="#9c9da1" stop-opacity="0.45"/>
          <stop offset="1" stop-color="#9c9da1" stop-opacity="0"/>
        </linearGradient>
      </defs>
      <polygon points="0,686 560,686 620,470 0,320" fill="url(#fold-dark)"/>
      <polygon points="560,686 1200,686 1200,360 620,470" fill="url(#fold-light)"/>
      <line x1="560" y1="686" x2="620" y2="470" stroke="var(--crease)" stroke-width="2"/>
    </svg>

    <h1 class="holder-name">Paul Verner, M.D.</h1>
    <p class="holder-title">-radiologist-</p>

    <div class="brand">
      <span class="brand-dot"></span>
      <p class="brand-name">Cedarpoint Imaging</p>
    </div>

    <dl class="contact-list">
      <dt>Phone:</dt><dd>936-555-0148</dd>
      <dt>Cell:</dt><dd>936-555-0148</dd>
      <dt>Fax:</dt><dd>936-555-0148</dd>
      <dt>Email:</dt><dd>office@brakwell-mail.net</dd>
    </dl>

    <address class="office-address">
      Cedarpoint Imaging, LLC.<br>
      48 Quill Ridge Lane<br>
      Montgomery, TX 77490<br>
      www.cedarpointimaging-demo.com
    </address>
  </main>
</body>
</html>
```